Birch Flooring Supply

Basic one-sided business card design using the attached logo. Vintage americana theme. Font is modified Arial Nova Cond, but anything that coordinates can be used

```html
<!DOCTYPE html>
<html lang="en">
<head>
<meta charset="utf-8">
<title>Birch Flooring Supply – Business Card</title>
<link href="https://fonts.googleapis.com/css2?family=Lato:wght@400;700&display=swap" rel="stylesheet">
<style>
  :root {
    --stage: #1b1b1b;
    --card: #050505;
    --gold: #b8936c;
    --ink: #ffffff;
    --ghost: rgba(255, 255, 255, 0.05);
  }
  * { margin: 0; padding: 0; box-sizing: border-box; }
  html, body {
    width: 1200px;
    height: 1059px;
    overflow: hidden;
    background: var(--stage);
    font-family: "Lato", Arial, sans-serif;
  }
  .canvas { position: relative; width: 1200px; height: 1059px; }

  .card {
    position: absolute;
    background: var(--card);
    border-radius: 24px;
    overflow: hidden;
    box-shadow: 0 14px 30px rgba(0, 0, 0, 0.6);
  }
  .card--front { left: 248px; top: 76px; width: 712px; height: 407px; }
  .card--back  { left: 252px; top: 546px; width: 707px; height: 401px; }

  .card__base-strip {
    position: absolute; left: 0; right: 0; bottom: 0; height: 8px;
    background: var(--gold);
  }

  /* brand mark: name in a plain circle */
  .brand {
    position: absolute;
    border-radius: 50%;
    border: 3px solid var(--gold);
    display: flex; flex-direction: column;
    align-items: center; justify-content: center;
    text-align: center;
    color: var(--ink);
    font-weight: 700;
    text-transform: uppercase;
    letter-spacing: 0.06em;
    line-height: 1.2;
  }
  .brand--small { left: 40px; top: 18px; width: 182px; height: 182px; font-size: 17px; }
  .brand--large { left: 217px; top: 70px; width: 272px; height: 272px; font-size: 25px; }
  .brand--ghost {
    left: 315px; top: 6px; width: 388px; height: 388px;
    border-color: var(--ghost); color: var(--ghost);
    font-size: 36px; border-width: 4px;
  }

  .name-accent {
    position: absolute; left: 0; top: 231px; width: 7px; height: 46px;
    background: var(--gold);
  }
  .person__name {
    position: absolute; left: 34px; top: 226px;
    font-size: 28px; font-weight: 700; color: var(--gold);
    letter-spacing: -0.02em; white-space: nowrap;
  }
  .person__role {
    position: absolute; left: 34px; top: 262px;
    font-size: 19px; font-weight: 400; color: var(--ink);
  }

  .contacts { position: absolute; left: 34px; top: 301px; list-style: none; }
  .contacts__item {
    display: flex; align-items: center; gap: 14px;
    height: 26px; font-size: 18px; color: var(--ink);
  }
  .contacts__icon { width: 20px; height: 20px; flex: none; }

  .address {
    position: absolute; right: 42px; top: 318px;
    text-align: right; font-size: 18px; line-height: 27px; color: var(--ink);
    font-style: normal;
  }
</style>
</head>
<body>
<main class="canvas">

  <section class="card card--front" aria-label="Business card front">
    <div class="brand brand--ghost" aria-hidden="true"><span>Birch</span><span>Flooring Supply</span></div>
    <div class="brand brand--small"><span>Birch</span><span>Flooring Supply</span></div>

    <span class="name-accent"></span>
    <h1 class="person__name">DANIEL HARPER</h1>
    <p class="person__role">Managing Director</p>

    <ul class="contacts">
      <li class="contacts__item">
        <svg class="contacts__icon" viewBox="0 0 24 24" fill="none" stroke="var(--ink)" stroke-width="2" stroke-linejoin="round">
          <path d="M5 3h4l2 5-2.5 1.5a11 11 0 0 0 6 6L16 13l5 2v4a2 2 0 0 1-2 2A16 16 0 0 1 3 5a2 2 0 0 1 2-2z"/>
        </svg>
        <span>071-555 0192</span>
      </li>
      <li class="contacts__item">
        <svg class="contacts__icon" viewBox="0 0 24 24">
          <rect x="2" y="5" width="20" height="14" fill="var(--ink)"/>
          <path d="M2 5l10 8 10-8" fill="none" stroke="var(--card)" stroke-width="1.8"/>
        </svg>
        <span>info@birchflooring.com</span>
      </li>
      <li class="contacts__item">
        <svg class="contacts__icon" viewBox="0 0 24 24" fill="none" stroke="var(--ink)" stroke-width="2">
          <circle cx="12" cy="12" r="9"/>
          <path d="M3 12h18M12 3c3 3 3 15 0 18M12 3c-3 3-3 15 0 18"/>
        </svg>
        <span>www.birchflooring.com</span>
      </li>
    </ul>

    <address class="address">
      18 Harbor Lane, Suite 4<br>Maple Ridge, 70318
    </address>

    <span class="card__base-strip"></span>
  </section>

  <section class="card card--back" aria-label="Business card back">
    <div class="brand brand--large"><span>Birch</span><span>Flooring Supply</span></div>
  </section>

</main>
</body>
</html>
```